Lorvika.no is a new website about pedagogical entrepreneurship. It's main target group is teachers. The Fjellmark Institute for Classroom Media and the Nordvik Agency for Schools and Study are leading the project.

The web page is meant to show examples of how different methods of entrepreneurship can be used pedagogical in a learning environment. The page will also support the user with examples of different teaching programs and other examples of best practice.

Pedagogical entrepreneurship is not about business and men in suits. It's a method for learning. The focus in the design should be on school, education and new ways of learning.

The final product should be motivating and engaging, but at the same time governmental and serious. We are not looking for something "flashy" and corporate-looking, but a moderate, task-focused and clean design that state quality.

We need designs for three pages:
1 - frontpage
2 - subpage ("Metoder og undervisningsopplegg")
3 - subpage ("Smått-VERK i Brekkelia")

The interaction design for these three pages will be uploaded as an attachment.

We would like you to find inspiration in the following websites:
- www.gryvekst.no
- www.lavrek.no
- www.tovandstudio.com
- www.kvp.no
(more will be added)

Please use the attached logo, and feel free to use this as an inspiration for the rest of the design.

Target Market(s)

Teachers

Industry/Entity Type

Education

Requirements
Must have
• * Header with: Logo. Main navigation. Utility navigation. Search box.
* Footer
Should not have
• Images of men in suits.
Very strong graphical elements that stands out too much (we want it clean).

```html
<!DOCTYPE html>
<html lang="en">
<head>
<meta charset="utf-8">
<title>Lorvika.no – Pedagogical entrepreneurship</title>
<link rel="stylesheet" href="https://fonts.googleapis.com/css2?family=Montserrat:wght@400;500;600;700&family=Noto+Serif:ital@1&display=swap">
<style>
:root{
  --blue:#2a8fd0;
  --blue-dark:#0c4a82;
  --navy:#0a3a68;
  --navy-deep:#0d4577;
  --green:#7fb227;
  --ink:#1d3b5c;
  --link:#1a66b0;
  --row:#f0f0f0;
  --white:#fff;
  --head:"Montserrat",sans-serif;
  --body:Arial,Helvetica,sans-serif;
  --serif:"Noto Serif",Georgia,serif;
}
*{box-sizing:border-box;margin:0;padding:0}
html,body{width:960px;height:1200px;overflow:hidden;background:var(--white)}
.page{position:relative;width:960px;height:1200px;font-family:var(--body);color:var(--ink)}
.abs{position:absolute}

/* header */
.brand{left:96px;top:30px;display:flex;align-items:center;gap:14px}
.brand-dot{width:50px;height:50px;border-radius:50%;background:var(--blue)}
.brand-name{font-family:var(--head);font-weight:700;font-size:38px;color:var(--blue);line-height:1}
.brand-tag{left:168px;top:70px;font-size:8px;color:var(--blue-dark)}
.social{left:376px;top:8px;display:flex;gap:12px}
.social span{display:inline-flex;align-items:center;font-size:9px;font-weight:700;color:#2e4a7a}
.social .btn{border:1px solid #c9c9c9;border-radius:2px;background:#f4f4f4;padding:2px 5px}
.social .count{border:1px solid #c9c9c9;border-radius:2px;padding:2px 4px;margin-left:3px;font-weight:400;color:#333}
.utility{left:549px;top:10px;width:315px;height:20px;border-bottom:1px dashed var(--green);display:flex;justify-content:space-between;padding:0 4px}
.utility a{font-size:9px;color:var(--link);text-decoration:none}

/* hero */
.hero{left:0;top:114px;width:960px;height:319px;background:radial-gradient(circle at 20% 40%,#3a9ad8,#1f7fc0 70%)}
.hero h1{left:93px;top:40px;font-family:var(--head);font-weight:700;font-size:49px;line-height:41px;color:var(--white);letter-spacing:.5px}
.hero p{left:93px;top:178px;width:360px;font-family:var(--head);font-size:14px;line-height:17.5px;color:var(--white)}
.hero .cta{left:93px;top:249px;width:139px;height:36px;border:2px solid var(--white);border-radius:20px;color:var(--white);font-family:var(--head);font-size:15px;display:flex;align-items:center;justify-content:center;background:#2587c8}
.hero-art{left:565px;top:24px;width:205px;height:295px;background:linear-gradient(180deg,#eaf4fb 0%,#cfe5f4 45%,#1a1a1a 60%,#111 100%);border-radius:90px 90px 0 0;opacity:.9}
.search-tab{left:677px;top:0;width:210px;height:37px;background:var(--blue-dark);border-radius:0 0 12px 12px;padding:6px 11px}
.search-field{width:187px;height:19px;background:var(--white);border-radius:10px;font-size:9px;color:#777;padding:4px 10px;position:relative}
.search-field svg{position:absolute;right:8px;top:4px}

/* feature band */
.band{left:0;top:433px;width:960px;height:106px;background:var(--blue-dark)}
.feature{position:absolute;top:19px;display:flex;align-items:center}
.feature-icon{width:68px;height:68px;border-radius:50%;border:3px solid var(--white);background:#2286c8;display:flex;align-items:center;justify-content:center;margin-right:10px}
.feature-text h3{font-family:var(--head);font-weight:500;font-size:12.5px;line-height:16px;color:var(--white)}
.feature-text em{font-family:var(--serif);font-size:11px;color:#4fb2ec}
.chev{position:absolute;top:28px}

/* meter */
.meter{left:117px;top:576px;width:160px;text-align:center}
.meter-dial{width:88px;height:88px;border-radius:50%;margin:0 auto 14px;background:radial-gradient(circle,#d9eefb 0%,#8ec8ec 55%,#0c4a82 58%,#0c4a82 64%,#c9ccd0 66%,#eef0f2 100%)}
.meter .q{font-family:var(--head);font-size:15px;color:#2b84c4;letter-spacing:.3px}
.meter .qb{font-family:var(--head);font-weight:700;font-size:14.5px;color:#2b84c4;padding-bottom:5px;border-bottom:1px dashed var(--green)}
.meter .try{font-family:var(--head);font-weight:600;font-size:12.5px;color:var(--green);margin-top:8px}

/* lists */
.lists{left:337px;top:578px;width:527px;height:211px;border:1px solid #ddd;border-top:none;border-radius:3px;display:flex}
.list{position:relative;width:50%}
.list+.list{border-left:1px solid #ddd}
.list-head{height:36px;background:var(--blue-dark);color:var(--white);font-family:var(--head);font-weight:500;font-size:14px;padding:10px 0 0 44px}
.list:first-child .list-head{border-radius:3px 0 0 0}
.list:last-child .list-head{border-radius:0 3px 0 0;padding-left:47px}
.ribbon{position:absolute;left:12px;top:-3px}
.list ul{list-style:none;margin-top:3px}
.list li{height:25.6px;display:flex;align-items:center;padding-left:44px;font-size:12px;color:var(--blue-dark)}
.list li:nth-child(odd){background:var(--row)}
.list li svg{margin-right:20px}
.view-more{position:absolute;left:21px;bottom:9px;width:77px;height:22px;border-radius:11px;background:linear-gradient(#3d9de0,#1a6fb6);color:var(--white);font-family:var(--head);font-size:9.5px;display:flex;align-items:center;justify-content:center;border:1px solid #0c4a82}

/* inspiration */
.rule{left:96px;top:820px;width:766px;border-top:1px dashed #8aa}
.insp-title{left:0;top:845px;width:960px;text-align:center;font-family:var(--head);font-weight:500;font-size:16px;color:var(--green);letter-spacing:.5px}
.carousel{left:126px;top:871px;width:718px;height:118px;background:var(--blue-dark)}
.arrow-btn{width:52px;height:52px;border-radius:50%;background:#f2f2f2;border:1px solid #ccc;top:904px}
.story{position:absolute;top:22px;display:flex;align-items:center}
.story-photo{width:78px;height:78px;border-radius:50%;border:3px solid var(--white);background:linear-gradient(180deg,#c9d3dc 0%,#9aa6a0 50%,#7a6a5c 100%);margin-right:6px}
.story-text{font-family:var(--body);font-weight:700;font-size:12.5px;line-height:16px;color:var(--white)}

/* footer */
.footer{left:0;top:1026px;width:960px;height:142px;background:var(--navy)}
.footer-mark{left:96px;top:22px;width:48px;height:48px;border-radius:50%;background:#3d9de0}
.fcol{position:absolute;top:16px}
.fcol h4{font-family:var(--head);font-weight:500;font-size:10.5px;color:var(--white);margin-bottom:10px;letter-spacing:.3px}
.fcol a{display:block;font-size:8.5px;color:#dfe9f3;text-decoration:none;line-height:22.4px}
.copyright{left:0;top:1168px;width:960px;height:32px;background:var(--navy-deep);padding:9px 96px;font-size:8.5px;color:var(--white)}
</style>
</head>
<body>
<div class="page">

  <!-- header -->
  <div class="abs brand"><span class="brand-dot"></span><span class="brand-name">Lorvika</span></div>
  <div class="abs brand-tag">Entreprenørielle metoder i undervisningen</div>
  <div class="abs social">
    <span><span class="btn">Like</span><span class="count">86</span></span>
    <span><span class="btn">Share</span><span class="count">30</span></span>
  </div>
  <nav class="abs utility">
    <a href="#">Home</a><a href="#">Best Practices Schools</a><a href="#">Lorvikameter</a><a href="#">About Lorvika.no</a>
  </nav>

  <section class="abs hero">
    <h1 class="abs">Pedagogical<br>entrepreneurship<br>works.</h1>
    <p class="abs">Lorem ipsum dolor sit amet, consectetur adipiscing elit. Etiam vitae nunc nec risus consectetur condimentum. Morbi justo metus.</p>
    <a class="abs cta">Learn More</a>
    <div class="abs hero-art" role="img" aria-label="Illustration of a figure holding up a cloud of learning and idea icons"></div>
    <div class="abs search-tab">
      <div class="search-field">search
        <svg width="10" height="10" viewBox="0 0 10 10"><circle cx="4" cy="4" r="3" fill="none" stroke="#1a6fb6" stroke-width="1.6"/><line x1="6.2" y1="6.2" x2="9" y2="9" stroke="#1a6fb6" stroke-width="1.8"/></svg>
      </div>
    </div>
  </section>

  <section class="abs band">
    <div class="feature" style="left:97px">
      <div class="feature-icon"><svg width="34" height="28" viewBox="0 0 34 28" fill="none" stroke="#fff" stroke-width="2"><path d="M2 3h12v22H2zM20 3h12v22H20z"/><path d="M14 6l6-3M14 25l6 3"/></svg></div>
      <div class="feature-text"><h3>What is Pedagogical<br>Entrepreneurship</h3><em>What, Why and How!</em></div>
    </div>
    <svg class="chev" style="left:323px" width="14" height="30" viewBox="0 0 14 30"><path d="M2 2l10 13L2 28" fill="none" stroke="#fff" stroke-width="1.6"/></svg>
    <div class="feature" style="left:365px">
      <div class="feature-icon"><svg width="36" height="30" viewBox="0 0 36 30" fill="none" stroke="#fff" stroke-width="2"><path d="M3 3h30v18H3zM18 21v6M12 28l6-6 6 6"/><path d="M8 9h14M8 14h10"/></svg></div>
      <div class="feature-text"><h3>Methods and<br>Teaching Plans</h3><em>Plan your Lessons!</em></div>
    </div>
    <svg class="chev" style="left:568px" width="14" height="30" viewBox="0 0 14 30"><path d="M2 2l10 13L2 28" fill="none" stroke="#fff" stroke-width="1.6"/></svg>
    <div class="feature" style="left:622px">
      <div class="feature-icon"><svg width="30" height="34" viewBox="0 0 30 34" fill="none" stroke="#fff" stroke-width="2"><path d="M4 2h18v28H4z"/><path d="M8 8h10M8 13h10M8 18h6"/><circle cx="22" cy="24" r="4"/></svg></div>
      <div class="feature-text"><h3>Good Examples,<br>Best Practices</h3><em>Be Inspired!</em></div>
    </div>
    <svg class="chev" style="left:833px" width="14" height="30" viewBox="0 0 14 30"><path d="M2 2l10 13L2 28" fill="none" stroke="#fff" stroke-width="1.6"/></svg>
  </section>

  <!-- meter -->
  <aside class="abs meter">
    <div class="meter-dial" role="img" aria-label="Meter dial graphic"></div>
    <div class="q">ARE YOU WORKING</div>
    <div class="qb">entrepreneurship-like</div>
    <div class="try">Try the Lorvikameter</div>
  </aside>

  <!-- lists -->
  <section class="abs lists">
    <div class="list">
      <svg class="ribbon" width="24" height="50" viewBox="0 0 24 50"><path d="M1 0h22v50L12 40 1 50z" fill="#b9c6d2" stroke="#8796a6"/><path d="M7 12h10M7 16h10M7 20h10M7 24h10" stroke="#0c4a82"/></svg>
      <div class="list-head">Methods</div>
      <ul>
        <li><svg width="14" height="8" viewBox="0 0 14 8"><path d="M0 2h8V0l6 4-6 4V6H0z" fill="#0c4a82"/></svg>Cafe-pedagogikk</li>
        <li><svg width="14" height="8" viewBox="0 0 14 8"><path d="M0 2h8V0l6 4-6 4V6H0z" fill="#0c4a82"/></svg>Elevbedrift</li>
        <li><svg width="14" height="8" viewBox="0 0 14 8"><path d="M0 2h8V0l6 4-6 4V6H0z" fill="#0c4a82"/></svg>Grundercamp</li>
        <li><svg width="14" height="8" viewBox="0 0 14 8"><path d="M0 2h8V0l6 4-6 4V6H0z" fill="#0c4a82"/></svg>Story line</li>
        <li><svg width="14" height="8" viewBox="0 0 14 8"><path d="M0 2h8V0l6 4-6 4V6H0z" fill="#0c4a82"/></svg>REAL</li>
      </ul>
      <a class="view-more">View More</a>
    </div>
    <div class="list">
      <svg class="ribbon" width="24" height="50" viewBox="0 0 24 50"><path d="M1 0h22v50L12 40 1 50z" fill="#b9c6d2" stroke="#8796a6"/><path d="M10 8v16a3 3 0 006 0V10" fill="none" stroke="#0c4a82" stroke-width="1.3"/></svg>
      <div class="list-head">Teaching Plans</div>
      <ul>
        <li><svg width="14" height="8" viewBox="0 0 14 8"><path d="M0 2h8V0l6 4-6 4V6H0z" fill="#0c4a82"/></svg>Teaching Plan Title</li>
        <li><svg width="14" height="8" viewBox="0 0 14 8"><path d="M0 2h8V0l6 4-6 4V6H0z" fill="#0c4a82"/></svg>Teaching Plan Title</li>
        <li><svg width="14" height="8" viewBox="0 0 14 8"><path d="M0 2h8V0l6 4-6 4V6H0z" fill="#0c4a82"/></svg>Teaching Plan Title</li>
        <li><svg width="14" height="8" viewBox="0 0 14 8"><path d="M0 2h8V0l6 4-6 4V6H0z" fill="#0c4a82"/></svg>Teaching Plan Title</li>
        <li><svg width="14" height="8" viewBox="0 0 14 8"><path d="M0 2h8V0l6 4-6 4V6H0z" fill="#0c4a82"/></svg>Teaching Plan Title</li>
      </ul>
      <a class="view-more">View More</a>
    </div>
  </section>

  <!-- inspiration -->
  <div class="abs rule"></div>
  <h2 class="abs insp-title">INSPIRATION</h2>
  <div class="abs arrow-btn" style="left:99px"><svg width="52" height="52" viewBox="0 0 52 52"><path d="M28 12L18 26l10 14" fill="none" stroke="#0c4a82" stroke-width="1.6"/></svg></div>
  <div class="abs arrow-btn" style="left:818px"><svg width="52" height="52" viewBox="0 0 52 52"><path d="M24 12l10 14-10 14" fill="none" stroke="#0c4a82" stroke-width="1.6"/></svg></div>
  <section class="abs carousel">
    <div class="story" style="left:34px"><div class="story-photo" role="img" aria-label="Photo of a school building with a tree in the yard"></div><div class="story-text">Smått-VERK at<br>Brekkelia school</div></div>
    <div class="story" style="left:259px"><div class="story-photo" role="img" aria-label="Photo of a school building with a tree in the yard"></div><div class="story-text">Smått-VERK at<br>Brekkelia school</div></div>
    <div class="story" style="left:492px"><div class="story-photo" role="img" aria-label="Photo of a school building with a tree in the yard"></div><div class="story-text">Smått-VERK at<br>Brekkelia school</div></div>
  </section>

  <!-- footer -->
  <footer class="abs footer">
    <div class="abs footer-mark"></div>
    <div class="fcol" style="left:186px"><h4>Pedagogical entrepreneurship</h4><a>What is pedagogical entrepreneurship</a><a>Science</a><a>Best Practice Schools</a><a>Lorvikameteret</a></div>
    <div class="fcol" style="left:385px"><h4>Methods</h4><a>Story line</a><a>REAL</a><a>Cafe-pedagogikk</a><a>see more</a></div>
    <div class="fcol" style="left:494px"><h4>Teaching Plans</h4><a>Title</a><a>Title</a><a>Title</a><a>see more</a></div>
    <div class="fcol" style="left:609px"><h4>Gode Eksempler</h4><a>Smått-VERK at Brekkelia school</a><a>Smått-VERK at Brekkelia school</a><a>Smått-VERK at Brekkelia school</a><a>see more</a></div>
    <div class="fcol" style="left:775px"><h4>About Lorvika.no</h4></div>
  </footer>
  <div class="abs copyright">Content copyright 2011 - 2012. Lorvika.no. All rights reserved.</div>

</div>
</body>
</html>
```